Marketing Flyer for Plumber Referals

8.5" x11" Layout should be landscape not portrait. Create a bold, eye-catching flyer that highlights earning potential from referrals for water damage restoration. Use high-contrast colors like blue, yellow, and white, with bold fonts and dynamic layouts. Include images of restoration work, cash, and happy clients. Emphasize key benefits like $500 minimum payouts, fast payments, and unlimited income potential. Keep instructions simple: refer a client, we handle the work, you get paid. Add a clear call-to-action and display contact details prominently. Focus on professionalism and energy.

Target Market(s)

Plumbers and Contractor 8.5" x11" Layout should be landscape not portrait.

Industry/Entity Type

General Contractor

Colors
0054AA
0677BA
7BADD7
CADEEF
E8F1F8
EB3D1F
EC4F4E
F09395
F8D3D4
FCEDEE

Requirements
Must have
• 8.5" x11" Layout should be landscape not portrait.
Nice to have

```html
<!DOCTYPE html>
<html lang="en">
<head>
<meta charset="utf-8">
<title>Flood Referral Flyers – Harbor Crest Builders</title>
<link href="https://fonts.googleapis.com/css2?family=Anton&family=Oswald:wght@400;500;700&family=Quicksand:wght@500&display=swap" rel="stylesheet">
<style>
  :root{
    --backdrop:#353535;
    --ink:#121212;
    --blue:#1c5cb6;
    --sky:#4aa8e8;
    --red:#ec1c24;
    --yellow:#ffe000;
    --white:#ffffff;
    --paper:#f1f1f1;
  }
  *{box-sizing:border-box;margin:0;padding:0}
  html,body{width:818px;height:1200px;overflow:hidden;background:var(--backdrop)}
  .stage{position:relative;width:818px;height:1200px}
  .flyer{position:absolute;left:49px;width:720px;height:556px;overflow:hidden;font-family:'Oswald',sans-serif}
  .front{top:30px;background:var(--paper)}
  .back{top:614px;background:var(--ink)}
  .abs{position:absolute}
  .headline{font-family:'Anton',sans-serif;font-weight:400;text-transform:uppercase;line-height:1}
  .brand{color:var(--white);font-size:9px;letter-spacing:.6px;text-align:center;font-weight:500;line-height:13px}
  .brand small{display:block;font-size:6px;letter-spacing:.8px;line-height:9px}

  /* front */
  .hero-photo{left:0;top:0;width:380px;height:470px;background:linear-gradient(100deg,#d7dadc 0%,#a9b0b5 35%,#c9cdd0 60%,#8e969c 100%)}
  .header-panel{left:30px;top:0;width:320px;height:330px;background:var(--ink);border-left:3px solid var(--white);border-right:3px solid var(--white);clip-path:polygon(0 0,100% 0,100% 86%,50% 100%,0 86%)}
  .brand-front{left:48px;top:26px;width:130px}
  .tagline{left:190px;top:18px;color:var(--white);font-size:22px;line-height:24px}
  .money-photo{left:70px;top:250px;width:240px;height:95px;background:radial-gradient(ellipse at center,#c7cdb8 0%,#a9b29c 60%,rgba(169,178,156,0) 100%)}
  .earn{left:0;width:380px;text-align:center;color:var(--red);-webkit-text-stroke:3px var(--white);paint-order:stroke fill;font-size:64px}
  .offer-bar{left:20px;top:372px;width:340px;height:56px;border:2px solid var(--white);display:flex}
  .offer-yellow{width:170px;background:var(--yellow);display:flex;align-items:center;padding-left:10px;gap:5px}
  .offer-red{flex:1;background:var(--red);display:flex;align-items:center;padding-left:24px;gap:6px}
  .big-num{font-family:'Anton',sans-serif;font-size:38px;line-height:1}
  .offer-yellow .big-num{color:var(--red)}
  .offer-red .big-num{color:var(--white)}
  .offer-small{font-size:12px;line-height:13px;color:var(--ink)}
  .offer-red .offer-small{color:var(--white)}
  .or-badge{left:176px;top:386px;width:28px;height:28px;border-radius:50%;background:var(--white);color:var(--ink);font-family:'Anton',sans-serif;font-size:13px;display:flex;align-items:center;justify-content:center;z-index:2}
  .partner-band{left:380px;top:0;width:340px;height:470px;background:var(--blue)}
  .partner-title{left:380px;top:26px;width:340px;text-align:center;color:var(--white);font-size:27px}
  .benefit{width:145px;height:162px;background:var(--white);clip-path:polygon(0 10px,100% 0,100% 100%,0 100%);text-align:center;padding-top:28px}
  .benefit-flag{width:30px;height:32px;background:var(--ink);clip-path:polygon(0 0,100% 0,100% 80%,0 100%);display:flex;align-items:flex-start;justify-content:center;padding-top:6px;z-index:2}
  .benefit h3{font-family:'Anton',sans-serif;font-weight:400;color:var(--red);font-size:18px;line-height:20px}
  .benefit p{font-size:11.5px;line-height:15px;color:#333;margin-top:8px;padding:0 10px}
  .benefit b{color:var(--ink)}
  .slogan-strip{left:0;top:470px;width:720px;height:30px;background:var(--ink);color:var(--white);font-family:'Anton',sans-serif;font-size:19px;text-align:center;line-height:30px}
  .cta-front{left:30px;top:504px;color:var(--blue);font-size:22px;line-height:24px}
  .contact{display:flex;align-items:center;gap:7px;line-height:1;white-space:nowrap}
  .dot{width:16px;height:16px;border-radius:50%;background:var(--yellow);display:flex;align-items:center;justify-content:center;flex:none}
  .front-contact{color:var(--red);font-family:'Anton',sans-serif}

  /* back */
  .top-white{left:0;top:0;width:720px;height:200px;background:var(--white)}
  .referrals-word{left:40px;top:10px;color:var(--sky);font-family:'Quicksand',sans-serif;font-size:56px;letter-spacing:1px;line-height:70px}
  .hand-photo{left:470px;top:40px;width:190px;height:160px;background:linear-gradient(160deg,#f3d9c6 0%,#e6bfa4 60%,#f5e6dc 100%);border-radius:40% 40% 0 0}
  .get-paid{left:40px;top:102px;color:var(--red);font-size:44px;line-height:46px}
  .blue-rule{left:0;top:200px;width:720px;height:5px;background:var(--blue)}
  .how-tab{left:220px;top:204px;width:280px;height:42px;background:var(--blue);clip-path:polygon(0 0,100% 0,94% 100%,6% 100%);color:var(--yellow);font-size:27px;text-align:center;line-height:42px}
  .step{top:268px;width:200px;height:190px;background:var(--white);text-align:center}
  .step-photo{height:80px}
  .step-num{top:258px;width:22px;height:28px;background:var(--red);border:2px solid var(--white);color:var(--white);font-family:'Anton',sans-serif;font-size:16px;line-height:24px;text-align:center}
  .step h3{color:var(--blue);font-weight:500;font-size:17px;line-height:19px;margin-top:8px}
  .step p{font-size:11px;line-height:14px;color:#222;margin-top:5px;padding:0 6px}
  .brand-back{left:40px;top:498px;width:220px;font-size:11px;line-height:15px}
  .brand-back small{font-size:7px;line-height:11px}
  .contact-panel{left:330px;top:466px;width:390px;height:90px;background:var(--blue);clip-path:polygon(8% 0,100% 0,100% 100%,0 100%)}
  .back-contact{left:378px;color:var(--white);font-family:'Anton',sans-serif}
</style>
</head>
<body>
<main class="stage">

  <!-- Front flyer -->
  <section class="flyer front" aria-label="Referral flyer, front">
    <div class="abs hero-photo" role="img" aria-label="Blurred photo of a flooded staircase"></div>
    <div class="abs header-panel"></div>
    <div class="abs brand brand-front">HARBOR CREST BUILDERS<small>COASTAL QUALITY BUILDERS</small></div>
    <div class="abs headline tagline">GET PAID TO<br>REFER A FLOOD</div>
    <div class="abs money-photo" role="img" aria-label="Photo of flying dollar bills"></div>
    <div class="abs headline earn" style="top:86px">Earn</div>
    <div class="abs headline earn" style="top:148px">Unlimited</div>
    <div class="abs headline earn" style="top:210px">Cash</div>

    <div class="abs offer-bar">
      <div class="offer-yellow"><span class="big-num">$500</span><span class="offer-small">Minimum</span></div>
      <div class="offer-red"><span class="big-num">10%</span><span class="offer-small">Per<br>Referral!</span></div>
    </div>
    <div class="abs or-badge">OR</div>

    <div class="abs partner-band"></div>
    <h2 class="abs headline partner-title">Why Partner With Us?</h2>

    <div class="abs benefit" style="left:397px;top:96px">
      <h3>Guaranteed<br>Payout</h3>
      <p>Minimum <b>$500</b> or <b>10%</b> of the invoice, paid fast.</p>
    </div>
    <div class="abs benefit" style="left:558px;top:96px">
      <h3>Free<br>Evaluations</h3>
      <p>We assess damage and process <b>insurance claims</b> for your clients.</p>
    </div>
    <div class="abs benefit" style="left:397px;top:294px">
      <h3>Industry<br>Leaders</h3>
      <p><b>Certified experts</b> with 24/7 rapid response.</p>
    </div>
    <div class="abs benefit" style="left:558px;top:294px">
      <h3>Affordable<br>Solutions</h3>
      <p><b>Lowest</b> out-of-pocket costs for your customers.</p>
    </div>
    <div class="abs benefit-flag" style="left:407px;top:82px"><svg width="15" height="15" viewBox="0 0 12 12"><circle cx="6" cy="6" r="5" fill="none" stroke="#fff" stroke-width="1.4"/><path d="M3.5 6.2l1.7 1.7 3.3-3.5" fill="none" stroke="#fff" stroke-width="1.4"/></svg></div>
    <div class="abs benefit-flag" style="left:568px;top:82px"><svg width="14" height="16" viewBox="0 0 11 13"><rect x="1" y="1" width="9" height="11" fill="none" stroke="#fff" stroke-width="1.2"/><path d="M3 4h5M3 6.5h5M3 9h3" stroke="#fff" stroke-width="1"/></svg></div>
    <div class="abs benefit-flag" style="left:407px;top:280px"><svg width="17" height="15" viewBox="0 0 14 12"><circle cx="7" cy="3" r="2.2" fill="#fff"/><circle cx="2.8" cy="5" r="1.7" fill="#fff"/><circle cx="11.2" cy="5" r="1.7" fill="#fff"/><rect x="1" y="8" width="12" height="3" fill="#fff"/></svg></div>
    <div class="abs benefit-flag" style="left:568px;top:280px"><svg width="16" height="16" viewBox="0 0 13 13"><circle cx="6.5" cy="5" r="3.5" fill="none" stroke="#fff" stroke-width="1.3"/><path d="M1 11c2-2 9-2 11 0" fill="none" stroke="#fff" stroke-width="1.3"/></svg></div>

    <div class="abs slogan-strip">SEND REFERRALS. GET PAID. GROW YOUR BUSINESS.</div>
    <div class="abs headline cta-front">CALL TEXT OR<br>BOOK ON-LINE</div>
    <div class="abs contact front-contact" style="left:290px;top:512px;font-size:32px">
      <span class="dot"><svg width="9" height="9" viewBox="0 0 8 8"><path d="M1 2.5C1 1.5 2 1 4 1s3 .5 3 1.5L6 3.5 5 3V2.3H3V3L2 3.5zM2 4h4l1 3H1z" fill="#121212"/></svg></span>555-214-7730
    </div>
    <div class="abs contact front-contact" style="left:500px;top:518px;font-size:20px">
      <span class="dot"><svg width="10" height="10" viewBox="0 0 10 10"><circle cx="5" cy="5" r="4" fill="none" stroke="#121212" stroke-width="1"/><path d="M1 5h8M5 1c-2 2.5-2 5.5 0 8M5 1c2 2.5 2 5.5 0 8" fill="none" stroke="#121212" stroke-width=".8"/></svg></span>HarborCrestBuild.com
    </div>
  </section>

  <!-- Back flyer -->
  <section class="flyer back" aria-label="Referral flyer, back">
    <div class="abs top-white"></div>
    <div class="abs hand-photo" role="img" aria-label="Photo of a hand writing with a blue marker"></div>
    <div class="abs referrals-word">REFERRALS</div>
    <svg class="abs" style="left:38px;top:80px" width="420" height="12" viewBox="0 0 420 12"><path d="M2 9C140 4 300 3 418 5" fill="none" stroke="#4aa8e8" stroke-width="4" stroke-linecap="round"/></svg>
    <h1 class="abs headline get-paid">Get Paid To Refer<br>A Flood</h1>
    <div class="abs blue-rule"></div>
    <h2 class="abs headline how-tab">HOW IT WORKS</h2>

    <div class="abs step" style="left:40px">
      <div class="step-photo" role="img" aria-label="Photo of a flooded home interior with stairs" style="background:linear-gradient(180deg,#c9b59a 0%,#8f7d68 55%,#4c5a5e 100%)"></div>
      <h3>Refer Flood,<br>Water and<br>Mold Damage</h3>
      <p>Call, book online or<br>text us directly.</p>
    </div>
    <div class="abs step" style="left:260px">
      <div class="step-photo" role="img" aria-label="Photo of an inspector holding a clipboard outside a house" style="background:linear-gradient(180deg,#b7c6d2 0%,#d9dee4 50%,#6f8a5c 100%)"></div>
      <h3>We Take Care<br>of Everything</h3>
      <p>Free evaluations,<br>insurance claims, and<br>professional service.</p>
    </div>
    <div class="abs step" style="left:480px">
      <div class="step-photo" role="img" aria-label="Photo of dollar bills with cash flow letter tiles" style="background:linear-gradient(135deg,#c8cfbf 0%,#9fab95 50%,#d4d9cc 100%)"></div>
      <h3>Get Paid<br>Fast</h3>
      <p>$500 minimum or 10%<br>of the invoice within<br>48 hours of final payment.</p>
    </div>
    <div class="abs step-num" style="left:52px">1</div>
    <div class="abs step-num" style="left:272px">2</div>
    <div class="abs step-num" style="left:492px">3</div>

    <div class="abs brand brand-back">HARBOR CREST BUILDERS<small>COASTAL QUALITY BUILDERS</small></div>
    <div class="abs contact-panel"></div>
    <div class="abs back-contact" style="top:474px;color:var(--yellow);font-size:17px;line-height:1">CALL TEXT OR BOOK ON-LINE</div>
    <div class="abs contact back-contact" style="top:497px;font-size:28px">
      <span class="dot"><svg width="9" height="9" viewBox="0 0 8 8"><path d="M1 2.5C1 1.5 2 1 4 1s3 .5 3 1.5L6 3.5 5 3V2.3H3V3L2 3.5zM2 4h4l1 3H1z" fill="#121212"/></svg></span>555-214-7730
    </div>
    <div class="abs contact back-contact" style="top:530px;font-size:18px">
      <span class="dot"><svg width="10" height="10" viewBox="0 0 10 10"><circle cx="5" cy="5" r="4" fill="none" stroke="#121212" stroke-width="1"/><path d="M1 5h8M5 1c-2 2.5-2 5.5 0 8M5 1c2 2.5 2 5.5 0 8" fill="none" stroke="#121212" stroke-width=".8"/></svg></span>HarborCrestBuild.com
    </div>
  </section>

</main>
</body>
</html>
```